Wrap design for Delivery van

I need a full Body wrap for a Korvath Limber Van 2013 model.
I will showcase the brand and color (as shown in attachment) and product images and product highlight messages. It will also show the contact information and message .

the background color should be white.

Target Market(s)

Food and Beverages

Industry/Entity Type

Food and Beverages

Colors
EB3D1F
EC4F4E
F09395
F8D3D4
FCEDEE

Requirements
Must have
• Product images

```html
<!DOCTYPE html>
<html lang="en">
<head>
<meta charset="utf-8">
<title>Leafmoor Plantain Chips – Korvath Limber Van Wrap</title>
<link rel="stylesheet" href="https://fonts.googleapis.com/css2?family=Lilita+One&family=Oswald:wght@500&family=Pacifico&family=Open+Sans:wght@400;600&display=swap">
<style>
  :root {
    --canvas: #ffffff;
    --wrap-red: #d93b39;
    --band-orange: #e2592a;
    --stripe-yellow: #d8d42c;
    --accent-yellow: #ece236;
    --title-white: #ffffff;
    --title-edge: #e8323a;
    --brand-green: #7db642;
    --photo-top: #f3efe6;
    --photo-mid: #d49a4a;
    --photo-low: #c9563a;
  }
  html, body {
    margin: 0;
    padding: 0;
    width: 1200px;
    height: 1200px;
    overflow: hidden;
    background: var(--canvas);
  }
  .wrap-sheet { display: block; width: 1200px; height: 1200px; }
  .panel-body { fill: var(--wrap-red); }
  .lower-band { fill: var(--band-orange); }
  .accent-stripe { fill: var(--stripe-yellow); }
  .brand-tab { fill: #ffffff; }
  .brand-name {
    font-family: "Open Sans", sans-serif;
    font-weight: 400;
    font-size: 32px;
    fill: var(--brand-green);
  }
  .product-title {
    font-family: "Lilita One", sans-serif;
    font-size: 74px;
    fill: var(--title-white);
    stroke: var(--title-edge);
    stroke-width: 4px;
    paint-order: stroke;
    letter-spacing: 1px;
  }
  .phone-number {
    font-family: "Oswald", sans-serif;
    font-weight: 500;
    font-size: 40px;
    font-style: italic;
    fill: var(--accent-yellow);
  }
  .phone-badge { fill: #ffffff; }
  .phone-glyph { fill: var(--band-orange); }
  .phone-arrow { fill: #ffffff; }
  .tagline {
    font-family: "Pacifico", cursive;
    font-size: 42px;
    fill: var(--accent-yellow);
  }
  .web-address {
    font-family: "Open Sans", sans-serif;
    font-weight: 600;
    font-size: 40px;
    fill: #ffffff;
    letter-spacing: 1px;
    text-anchor: middle;
  }
</style>
</head>
<body>
<svg class="wrap-sheet" viewBox="0 0 1200 1200" xmlns="http://www.w3.org/2000/svg">
  <defs>
    <linearGradient id="bag-tones" x1="0" y1="0" x2="0" y2="1">
      <stop offset="0" stop-color="var(--photo-top)"/>
      <stop offset="0.45" stop-color="var(--photo-mid)"/>
      <stop offset="1" stop-color="var(--photo-low)"/>
    </linearGradient>
    <clipPath id="side-top"><rect x="40" y="110" width="1120" height="420" rx="28"/></clipPath>
    <clipPath id="side-bottom"><rect x="40" y="650" width="1120" height="420" rx="28"/></clipPath>
  </defs>

  <!-- Side A: curved stripe version -->
  <g class="wrap-side wrap-side--curved" clip-path="url(#side-top)">
    <rect class="panel-body" x="40" y="110" width="1120" height="420"/>
    <path class="lower-band" d="M40 424 C 350 419, 550 459, 760 466 C 950 472, 1080 462, 1160 458 L 1160 530 L 40 530 Z"/>
    <path class="accent-stripe" d="M40 410 C 350 405, 550 445, 760 452 C 950 458, 1080 448, 1160 444 L 1160 458 C 1080 462, 950 472, 760 466 C 550 459, 350 419, 40 424 Z"/>
    <g role="img" aria-label="Product photos of two plantain chip bags">
      <rect x="80" y="128" width="160" height="170" rx="10" fill="url(#bag-tones)" transform="rotate(-8 160 213)"/>
      <rect x="170" y="262" width="170" height="140" rx="10" fill="url(#bag-tones)" transform="rotate(-4 255 332)"/>
    </g>
    <path class="brand-tab" d="M400 110 H620 V168 q-5 7 -10 0 t-10 0 t-10 0 t-10 0 t-10 0 t-10 0 t-10 0 t-10 0 t-10 0 t-10 0 t-10 0 t-10 0 t-10 0 t-10 0 t-10 0 t-10 0 t-10 0 t-10 0 t-10 0 t-10 0 t-10 0 t-10 0 Z"/>
    <circle cx="432" cy="144" r="7" fill="var(--brand-green)"/>
    <text class="brand-name" x="448" y="155">Leafmoor</text>
    <text class="product-title" x="380" y="250">PLANTAIN</text>
    <text class="product-title" x="380" y="322">CHIPS</text>
    <g class="phone-icon">
      <circle class="phone-badge" cx="402" cy="374" r="21"/>
      <path class="phone-glyph" d="M393 363 l5 -2 l4 7 l-4 3 q3 6 8 9 l3 -4 l7 4 l-2 5 q-15 0 -21 -22 z"/>
      <path class="phone-arrow" d="M430 365 l8 9 l-8 9 z"/>
    </g>
    <text class="phone-number" x="448" y="389">234-555-014-7720</text>
    <text class="tagline" x="820" y="300">Healthy</text>
    <text class="tagline" x="850" y="370">Snack !</text>
    <text class="web-address" x="720" y="512">www.leafmoor.farm</text>
  </g>

  <!-- Side B: straight stripe version -->
  <g class="wrap-side wrap-side--straight" clip-path="url(#side-bottom)">
    <rect class="panel-body" x="40" y="650" width="1120" height="420"/>
    <rect class="accent-stripe" x="40" y="996" width="1120" height="12"/>
    <rect class="lower-band" x="40" y="1008" width="1120" height="62"/>
    <g role="img" aria-label="Product photos of two plantain chip bags">
      <rect x="80" y="668" width="160" height="170" rx="10" fill="url(#bag-tones)" transform="rotate(-8 160 753)"/>
      <rect x="170" y="802" width="170" height="150" rx="10" fill="url(#bag-tones)" transform="rotate(-4 255 877)"/>
    </g>
    <path class="brand-tab" d="M400 650 H620 V708 q-5 7 -10 0 t-10 0 t-10 0 t-10 0 t-10 0 t-10 0 t-10 0 t-10 0 t-10 0 t-10 0 t-10 0 t-10 0 t-10 0 t-10 0 t-10 0 t-10 0 t-10 0 t-10 0 t-10 0 t-10 0 t-10 0 t-10 0 Z"/>
    <circle cx="432" cy="684" r="7" fill="var(--brand-green)"/>
    <text class="brand-name" x="448" y="695">Leafmoor</text>
    <text class="product-title" x="380" y="790">PLANTAIN</text>
    <text class="product-title" x="380" y="862">CHIPS</text>
    <text class="phone-number" x="384" y="932">234-555-014-7720</text>
    <text class="tagline" x="820" y="840">Healthy</text>
    <text class="tagline" x="850" y="910">Snack !</text>
    <text class="web-address" x="720" y="1053">www.leafmoor.farm</text>
  </g>
</svg>
</body>
</html>
```